Adwords Banner for unique handmade Jewelery

We need one Banner for our Jewelerys
in 4 sizes:
300x250px
336x280px
728x90px
160x600px

http://www.fenka-lauro.de/schmuck/2/

```html
<!DOCTYPE html>
<html lang="de">
<head>
<meta charset="utf-8">
<title>fenka&amp;lauro – Banner Set</title>
<link rel="stylesheet" href="https://fonts.googleapis.com/css2?family=Quicksand:wght@500&family=Italianno&family=Arimo&display=swap">
<style>
  :root {
    --page: #ffffff;
    --label: #111111;
    --brand-grey: #7d7d82;
    --tagline-pink: #c2667f;
    --tab-white: #fbfbfc;
    --tab-edge: #d9d9de;
    --bead-pink: #d25a74;
    --bead-rose: #e89aaa;
    --silver: #dfe0e6;
    --silver-deep: #a9abb4;
  }
  * { margin: 0; padding: 0; box-sizing: border-box; }
  html, body { width: 1200px; height: 900px; overflow: hidden; background: var(--page); }
  .sheet { position: relative; width: 1200px; height: 900px; }
  .size-label {
    position: absolute;
    font-family: "Arimo", sans-serif;
    font-size: 15px;
    letter-spacing: 1px;
    color: var(--label);
  }
  .banner { position: absolute; overflow: hidden; }
  .banner svg { display: block; width: 100%; height: 100%; }
  .brand-name { font-family: "Quicksand", sans-serif; font-weight: 500; fill: var(--brand-grey); }
  .tagline { font-family: "Italianno", cursive; fill: var(--tagline-pink); letter-spacing: 1.5px; }
  .tab { fill: var(--tab-white); stroke: var(--tab-edge); stroke-width: 1; }

  .banner-medium { left: 61px; top: 164px; width: 352px; height: 293px; }
  .banner-large  { left: 445px; top: 164px; width: 394px; height: 328px; }
  .banner-leader { left: 61px; top: 550px; width: 852px; height: 115px; }
  .banner-sky    { left: 938px; top: 105px; width: 188px; height: 703px; }
</style>
</head>
<body>
<main class="sheet">
  <svg width="0" height="0" style="position:absolute" aria-hidden="true">
    <defs>
      <linearGradient id="bead-photo-h" x1="0" y1="0" x2="1" y2="0">
        <stop offset="0" stop-color="#d9687f"/>
        <stop offset="0.25" stop-color="#eef0f4"/>
        <stop offset="0.45" stop-color="#b9bbc4"/>
        <stop offset="0.6" stop-color="#e6e7ec"/>
        <stop offset="0.8" stop-color="#d25a74"/>
        <stop offset="1" stop-color="#f0eef2"/>
      </linearGradient>
      <linearGradient id="bead-photo-v" x1="0" y1="0" x2="0" y2="1">
        <stop offset="0" stop-color="#d25a74"/>
        <stop offset="0.3" stop-color="#c9cbd3"/>
        <stop offset="0.5" stop-color="#d96c83"/>
        <stop offset="0.7" stop-color="#e4e5ea"/>
        <stop offset="0.9" stop-color="#b8bac2"/>
        <stop offset="1" stop-color="#e8a3b1"/>
      </linearGradient>
    </defs>
  </svg>

  <span class="size-label" style="left:61px;top:141px">300 x 250</span>
  <div class="banner banner-medium">
    <svg viewBox="0 0 300 250" preserveAspectRatio="none">
      <rect width="300" height="250" fill="url(#bead-photo-h)" role="img" aria-label="Close-up photo of a bracelet with pink glass beads and polished silver beads"/>
      <polygon class="tab" points="20,0 282,0 252,44 50,44"/>
      <text class="brand-name" x="151" y="29" font-size="23" text-anchor="middle">fenka&amp;lauro</text>
      <polygon class="tab" points="35,250 62,210 282,210 300,228 300,250"/>
      <text class="tagline" x="170" y="238" font-size="22" text-anchor="middle">Einzigartig: Der Schmuck</text>
    </svg>
  </div>

  <span class="size-label" style="left:445px;top:141px">338 x 280</span>
  <div class="banner banner-large">
    <svg viewBox="0 0 338 280" preserveAspectRatio="none">
      <rect width="338" height="280" fill="url(#bead-photo-h)" role="img" aria-label="Close-up photo of a bracelet with pink glass beads and polished silver beads"/>
      <polygon class="tab" points="24,0 316,0 284,48 56,48"/>
      <text class="brand-name" x="170" y="32" font-size="26" text-anchor="middle">fenka&amp;lauro</text>
      <polygon class="tab" points="40,280 70,235 318,235 338,255 338,280"/>
      <text class="tagline" x="192" y="266" font-size="25" text-anchor="middle">Einzigartig: Der Schmuck</text>
    </svg>
  </div>

  <span class="size-label" style="left:63px;top:518px">728 x 90</span>
  <div class="banner banner-leader">
    <svg viewBox="0 0 728 90" preserveAspectRatio="none">
      <rect width="728" height="90" fill="url(#bead-photo-h)" role="img" aria-label="Close-up photo of a bracelet with pink glass beads and polished silver beads"/>
      <polygon class="tab" points="40,0 300,0 266,52 82,52"/>
      <text class="brand-name" x="174" y="30" font-size="22" text-anchor="middle">fenka&amp;lauro</text>
      <polygon class="tab" points="452,90 478,64 728,64 728,90"/>
      <text class="tagline" x="600" y="84" font-size="19" text-anchor="middle">Einzigartig: Der Schmuck</text>
    </svg>
  </div>

  <span class="size-label" style="left:938px;top:80px">160 x 600</span>
  <div class="banner banner-sky">
    <svg viewBox="0 0 160 600" preserveAspectRatio="none">
      <rect width="160" height="600" fill="url(#bead-photo-v)" role="img" aria-label="Close-up photo of a bracelet with pink glass beads and polished silver beads"/>
      <polygon class="tab" points="160,20 160,300 132,276 132,46"/>
      <text class="tagline" transform="translate(153,160) rotate(-90)" font-size="21" text-anchor="middle">Einzigartig: Der Schmuck</text>
      <polygon class="tab" points="0,300 55,336 55,568 0,600"/>
      <text class="brand-name" transform="translate(36,452) rotate(-90)" font-size="24" text-anchor="middle">fenka&amp;lauro</text>
    </svg>
  </div>
</main>
</body>
</html>
```